Four in One (Flexible infographic for Content Management Industry)

See attachment.
A graphic depicting 4 products, where each can stand on its own and each can be combined with others, but where, if all are taken together, the best result is achieved (the "super product").
Intended use is web. See attached file as an example.
The most basic idea is as the attached diagram shows, where 4 rectangles are arranged in a quadrangle, with a middle rectangle in the center representing the combined 4 products. This concept is fine except it is a bit too obvious as it stands. We are looking for either a variation of this or another concept.
The audience is technical + professional + enterprise - NOT consumers. Hence the design should be conservative in nature.
We are aware of tools like as Canva or Pictogram where such graphics are available, but we are looking for something with a bit more imagination and flexibility.
This graphic should be targeted to web sites and be delivered with vector-based (SVG) graphics.

```html
<!DOCTYPE html>
<html lang="en">
<head>
<meta charset="utf-8">
<title>Super Product – Four in One</title>
<link rel="stylesheet" href="https://fonts.googleapis.com/css2?family=Arimo:wght@400;700&family=Oswald:wght@500&display=swap">
<style>
  :root {
    --bg: #f7f7f7;
    --ink: #111111;
    --orange: #ffa02e;
    --red: #e8204e;
    --magenta: #a0216a;
    --lilac: #9d60e0;
  }
  * { margin: 0; padding: 0; box-sizing: border-box; }
  html, body { width: 1200px; height: 529px; overflow: hidden; background: var(--bg); }
  .infographic { position: relative; width: 1200px; height: 529px; font-family: "Arimo", Arial, sans-serif; color: var(--ink); }
  .diagram { position: absolute; left: 0; top: 0; }

  .feature { position: absolute; width: 330px; }
  .feature--left { text-align: left; }
  .feature--right { text-align: right; }
  .feature__title { font-weight: 700; font-size: 24px; line-height: 24px; letter-spacing: 0.2px; text-transform: uppercase; }
  .feature__text { margin-top: 20px; font-size: 12.7px; line-height: 15px; width: 275px; }
  .feature--right .feature__text { margin-left: auto; }
  .feature__list { list-style: none; margin-top: 11px; font-size: 12.7px; line-height: 18px; }
  .feature--left .feature__list li::before {
    content: ""; display: inline-block; margin-right: 6px; vertical-align: 1px;
    border-left: 5px solid var(--accent); border-top: 3px solid transparent; border-bottom: 3px solid transparent;
  }
  .feature--right .feature__list li::after {
    content: ""; display: inline-block; margin-left: 6px; vertical-align: 1px;
    border-right: 5px solid var(--accent); border-top: 3px solid transparent; border-bottom: 3px solid transparent;
  }

  .feature--documents { left: 125px; top: 70px; --accent: var(--red); }
  .feature--documents .feature__title { color: var(--red); }
  .feature--security { left: 746px; top: 70px; --accent: var(--magenta); }
  .feature--security .feature__title { color: var(--magenta); }
  .feature--erp { left: 66px; top: 275px; --accent: var(--orange); }
  .feature--digital { left: 804px; top: 275px; --accent: var(--lilac); }

  .core-label {
    position: absolute; left: 500px; top: 364px; width: 200px; text-align: center;
    font-family: "Oswald", "Arial Narrow", sans-serif; font-weight: 500; font-size: 40px; line-height: 40px; letter-spacing: 0.5px;
  }
</style>
</head>
<body>
<main class="infographic">
  <svg class="diagram" width="1200" height="529" viewBox="0 0 1200 529" aria-hidden="true">
    <!-- connector lines -->
    <g fill="none" stroke-width="1.2">
      <polyline points="125,125 402,125 511,226" stroke="var(--red)"/>
      <polyline points="1076,125 799,125 689,226" stroke="var(--magenta)"/>
      <polyline points="66,328 353,328 382,353" stroke="var(--orange)"/>
      <polyline points="1134,328 846,328 818,353" stroke="var(--lilac)"/>
    </g>
    <g stroke-width="4">
      <line x1="125" y1="125" x2="167" y2="125" stroke="var(--red)"/>
      <line x1="1034" y1="125" x2="1076" y2="125" stroke="var(--magenta)"/>
      <line x1="66" y1="328" x2="109" y2="328" stroke="var(--orange)"/>
      <line x1="1090" y1="328" x2="1134" y2="328" stroke="var(--lilac)"/>
    </g>

    <!-- outer arc -->
    <g fill="none" stroke-width="6">
      <path d="M363,446 A237,237 0 0 1 405.9,310.1" stroke="var(--orange)"/>
      <path d="M405.9,310.1 A237,237 0 0 1 600,209" stroke="var(--red)"/>
      <path d="M600,209 A237,237 0 0 1 786.8,300.1" stroke="var(--magenta)"/>
      <path d="M786.8,300.1 A237,237 0 0 1 837,446" stroke="var(--lilac)"/>
    </g>
    <circle cx="381.8" cy="353.4" r="6.5" fill="var(--orange)"/>
    <circle cx="511.2" cy="226.3" r="6.5" fill="var(--red)"/>
    <circle cx="688.8" cy="226.3" r="6.5" fill="var(--magenta)"/>
    <circle cx="818.2" cy="353.4" r="6.5" fill="var(--lilac)"/>

    <!-- product segments -->
    <g stroke="var(--bg)" stroke-width="7" stroke-linejoin="miter">
      <path d="M403,446 A197,197 0 0 1 460.7,306.7 L534.9,380.9 A92,92 0 0 0 508,446 Z" fill="var(--orange)"/>
      <path d="M460.7,306.7 A197,197 0 0 1 600,249 L600,354 A92,92 0 0 0 534.9,380.9 Z" fill="var(--red)"/>
      <path d="M600,249 A197,197 0 0 1 739.3,306.7 L665.1,380.9 A92,92 0 0 0 600,354 Z" fill="var(--magenta)"/>
      <path d="M739.3,306.7 A197,197 0 0 1 797,446 L692,446 A92,92 0 0 0 665.1,380.9 Z" fill="var(--lilac)"/>
    </g>

    <!-- segment icons -->
    <g fill="none" stroke="#fff" stroke-width="1.8" stroke-linecap="round" stroke-linejoin="round">
      <!-- enterprise: building with finance marks -->
      <g transform="translate(462,393)">
        <rect x="-10" y="-2" width="20" height="24"/>
        <rect x="-19" y="8" width="9" height="14"/>
        <rect x="10" y="8" width="9" height="14"/>
        <path d="M-5,4h3M2,4h3M-5,10h3M2,10h3M-3,22v-6h6v6"/>
        <circle cx="0" cy="-19" r="6"/>
        <circle cx="-17" cy="-10" r="5"/>
        <circle cx="17" cy="-10" r="5"/>
        <path d="M-10,-2 L-3,-8 L3,-5 L9,-11"/>
      </g>
      <!-- documents: window with folders and gear -->
      <g transform="translate(545,314)">
        <rect x="-20" y="-20" width="40" height="34" rx="2"/>
        <path d="M-20,-13h40"/>
        <rect x="-15" y="-8" width="8" height="6"/>
        <rect x="-4" y="-8" width="8" height="6"/>
        <rect x="7" y="-8" width="8" height="6"/>
        <rect x="-4" y="2" width="8" height="6"/>
        <rect x="7" y="2" width="8" height="6"/>
        <circle cx="-12" cy="12" r="8" fill="var(--red)"/>
        <circle cx="-12" cy="12" r="3"/>
      </g>
      <!-- security: documents with shield lock -->
      <g transform="translate(655,314)">
        <rect x="-16" y="-20" width="24" height="30" rx="2"/>
        <rect x="-20" y="-15" width="24" height="30" rx="2" fill="var(--magenta)"/>
        <path d="M-15,-8h14M-15,-3h14M-15,2h8"/>
        <path d="M10,-2 L20,2 V10 C20,16 15,20 10,22 C5,20 0,16 0,10 V2 Z" fill="var(--magenta)"/>
        <rect x="6" y="8" width="8" height="6"/>
        <path d="M8,8v-2a2,2 0 0 1 4,0v2"/>
      </g>
      <!-- digital: monitor with bar chart -->
      <g transform="translate(735,392)">
        <rect x="-22" y="-18" width="38" height="28" rx="2"/>
        <path d="M-22,-12h38M-7,10v6M-12,16h10"/>
        <path d="M-16,6v-4M-12,6v-7M-8,6v-10M-4,6v-13M0,6v-8"/>
        <path d="M16,-8h6M16,0h8M16,-16h6"/>
        <circle cx="24" cy="-16" r="1.5"/>
        <circle cx="26" cy="0" r="1.5"/>
      </g>
    </g>
  </svg>

  <section class="feature feature--left feature--documents">
    <h2 class="feature__title">Document<br>Management</h2>
    <p class="feature__text">Streamline document organization, access, and collaboration with easier file storage and sharing, leading to more efficient workflows.</p>
    <ul class="feature__list">
      <li>Centralized Document Control</li>
      <li>Collaborative Workspace Integration</li>
      <li>Automated Compliance Tracking</li>
      <li>Check 4</li>
    </ul>
  </section>

  <section class="feature feature--right feature--security">
    <h2 class="feature__title">Security and<br>Compliance</h2>
    <p class="feature__text">Benefit from tailored cloud solutions, secure data storage, and expert disaster recovery planning for reliable and scalable IT operations.</p>
    <ul class="feature__list">
      <li>Custom Cloud Solutions</li>
      <li>Secure Data Storage</li>
      <li>Expert Disaster Recovery</li>
      <li>Check 4</li>
    </ul>
  </section>

  <section class="feature feature--left feature--erp">
    <h2 class="feature__title">Enterprise<br>Resource Planning</h2>
    <p class="feature__text">Simplify management across finance, sales, and operations, enabling better decision-making and improved productivity.</p>
    <ul class="feature__list">
      <li>Integrated Business Processes</li>
      <li>Enhanced Decision-Making</li>
      <li>Productivity Improvement</li>
      <li>Check 4</li>
    </ul>
  </section>

  <section class="feature feature--right feature--digital">
    <h2 class="feature__title">Digitital<br>Transformation</h2>
    <p class="feature__text">Turn scanned documents into easily searchable digital archives, boosting efficiency and accessibility.</p>
    <ul class="feature__list">
      <li>Instant searchable Archives with OCR</li>
      <li>Automated Document Classification</li>
      <li>DocuHub and Cloud Blob Ready</li>
      <li>Check 4</li>
    </ul>
  </section>

  <h1 class="core-label">SUPER<br>PRODUCT</h1>
</main>
</body>
</html>
```